amber crest health and wellness group.

need a full website design , all information provided in word document labeled website blue print

Target Market(s)

first responders, military , people in crisis

Coding

Coded - Design and coding required

Number of Pages Required

1 page

```html
<!DOCTYPE html>
<html lang="en">
<head>
<meta charset="utf-8">
<title>Amber Crest Health &amp; Wellness Group</title>
<link href="https://fonts.googleapis.com/css2?family=Montserrat:wght@400;500;600;700;800&display=swap" rel="stylesheet">
<style>
:root{
  --blue:#245e9f;
  --blue-dark:#1c4f8a;
  --blue-deep:#163f70;
  --ink:#1b1b1b;
  --text:#555;
  --muted:#8a8a8a;
  --card:#a3a3a3;
  --footer:#1b1b1b;
  --white:#fff;
}
*{box-sizing:border-box;margin:0;padding:0}
html,body{width:1200px;height:3630px;overflow:hidden}
body{font-family:"Montserrat",sans-serif;color:var(--ink);background:#fff;position:relative}
.abs{position:absolute}
.btn{position:absolute;display:flex;align-items:center;justify-content:center;gap:14px;font-size:11px;font-weight:600;letter-spacing:.2px;text-transform:uppercase;border-radius:2px}
.btn svg{width:12px;height:12px}
.btn-blue{background:var(--blue);color:#fff}
.btn-grey{background:#9a9a9a;color:#fff}
.btn-white{background:#fff;color:var(--blue)}
.eyebrow{font-size:11px;color:var(--muted);text-transform:uppercase;letter-spacing:.3px;display:flex;align-items:center;gap:8px}
.eyebrow .rule{width:52px;height:1px;background:#aaa}
.accent{color:var(--blue)}

/* top bar */
.topbar{left:0;top:0;width:1200px;height:24px;background:var(--blue);color:#fff;font-size:10px;display:flex;align-items:center;justify-content:center}

/* hero */
.hero{left:0;top:24px;width:1200px;height:592px;background:linear-gradient(90deg,#1d2d40 0%,#3b4d60 40%,#8e8c86 65%,#5a4a7a 85%,#4a4060 100%)}
.hero-shade{left:0;top:0;width:1200px;height:592px;background:linear-gradient(90deg,rgba(20,34,52,.85) 0%,rgba(20,34,52,.5) 45%,rgba(20,34,52,0) 70%)}
.brand{display:flex;flex-direction:column;align-items:center;color:var(--blue);font-weight:700;text-transform:uppercase;line-height:1.1;text-align:center}
.brand .name{font-size:17px;letter-spacing:.5px}
.brand .sub{font-size:6px;letter-spacing:.4px}
.brand .mark{width:40px;height:40px;border-radius:50%;background:#b9bfc6;margin-bottom:6px}
.nav{left:562px;top:59px;display:flex;gap:37px;font-size:11px;font-weight:600;color:#fff;text-transform:uppercase}
.nav .active{color:#6aa4e6}
.hero-eyebrow{left:120px;top:211px;color:#d9dee4}
.hero-eyebrow .rule{background:#d9dee4}
.hero h1{position:absolute;left:118px;top:234px;font-size:45px;line-height:53px;font-weight:600;color:#fff;letter-spacing:.5px}
.hero p{position:absolute;left:120px;top:351px;width:450px;font-size:11px;line-height:17px;color:#fff}

/* about */
.about-photo{left:148px;top:744px;width:316px;height:316px;border-radius:50%;border:8px solid var(--blue);padding:4px;background:#fff}
.about-photo div{width:100%;height:100%;border-radius:50%;background:linear-gradient(135deg,#c9b59d 0%,#8a6a52 45%,#3d3a3a 100%)}
.about-eyebrow{left:608px;top:698px}
.about h2{position:absolute;left:608px;top:720px;font-size:30px;line-height:36px;font-weight:600;letter-spacing:.3px}
.about .tag{position:absolute;left:610px;top:802px;font-size:10.5px;font-weight:600;color:var(--blue);text-transform:uppercase}
.about p{position:absolute;left:608px;top:831px;width:400px;font-size:10.5px;line-height:18.5px;color:var(--text)}
.about p b{color:var(--ink);font-weight:600}
.about .ghost{position:absolute;left:606px;top:980px;font-size:64px;font-weight:800;color:#eef1f5;letter-spacing:1px;white-space:nowrap}

/* mission band */
.mission{left:0;top:1111px;width:1200px;height:311px;background:linear-gradient(180deg,var(--blue) 0%,var(--blue-dark) 100%)}
.emblem{left:476px;top:1140px;width:248px;height:248px;border-radius:50%;background:#3d76b8;display:flex;align-items:center;justify-content:center}
.emblem div{width:220px;height:220px;border-radius:50%;background:#fff;display:flex;align-items:center;justify-content:center;color:var(--blue);font-weight:700;font-size:22px;text-align:center;line-height:1.15}
.mv{position:absolute;width:290px;color:#fff}
.mv svg{width:48px;height:48px}
.mv h3{font-size:23px;font-weight:600;margin-top:8px;letter-spacing:.3px}
.mv p{font-size:10.5px;line-height:18px;margin-top:4px}

/* services */
.services-bg{left:0;top:1422px;width:1200px;height:820px;background:linear-gradient(180deg,#fff 0%,#fff 55%,#e5ecf6 100%)}
.center-eyebrow{left:0;width:1200px;justify-content:center}
.section-title{position:absolute;left:0;width:1200px;text-align:center;font-size:30px;font-weight:600;letter-spacing:.3px;line-height:36px}
.card{position:absolute;width:228px;height:217px;background:var(--card);border-radius:3px;padding:6px}
.card.feature{background:var(--blue)}
.card .ph{width:216px;height:134px;background:linear-gradient(135deg,#6b5a4a,#2e2a28)}
.card .icon{position:absolute;left:90px;top:116px;width:48px;height:48px;border-radius:50%;background:#fff;display:flex;align-items:center;justify-content:center}
.card .icon span{width:30px;height:30px;border-radius:50%;background:var(--blue);display:flex;align-items:center;justify-content:center}
.card .icon svg{width:16px;height:16px}
.card h4{position:absolute;left:0;top:172px;width:228px;text-align:center;color:#fff;font-size:15px;font-weight:500;line-height:18px}
.card h4.one{top:181px}

/* who we serve */
.serve{position:absolute;width:320px}
.serve h5{font-size:15px;font-weight:500;display:flex;align-items:center;gap:7px}
.serve h5 svg{width:14px;height:14px;flex:none}
.serve p{margin-left:21px;font-size:10.5px;line-height:14px;color:var(--text);margin-top:5px;width:210px}

/* partners */
.partners{left:145px;top:2764px;width:910px;height:97px;border:1.5px solid var(--blue);display:flex}
.partner{flex:1;border-right:1.5px solid var(--blue);display:flex;align-items:center;justify-content:center;gap:8px;font-size:13px;font-weight:600;color:#3f5e80}
.partner:last-child{border-right:0}
.partner i{width:20px;height:20px;border-radius:50%;background:#b9d3a0;display:block}
.arrow{position:absolute;width:14px;height:14px}

/* cta */
.cta{left:0;top:2960px;width:1200px;height:352px;background:var(--blue)}
.cta-person{left:556px;top:2915px;width:400px;height:397px;border-radius:200px 200px 0 0;background:linear-gradient(180deg,#6b4a3a 0%,#e9e6e2 35%,#f4f4f4 100%)}
.cta h2{position:absolute;left:139px;top:3015px;font-size:30px;line-height:37px;font-weight:600;color:#fff}
.cta p{position:absolute;left:142px;top:3095px;width:320px;font-size:11px;line-height:18px;color:#fff}

/* footer */
.footer{left:0;top:3312px;width:1200px;height:318px;background:var(--footer);color:#fff}
.fcol{position:absolute}
.fcol h6{font-size:15px;font-weight:600;text-transform:uppercase;letter-spacing:.2px}
.fcol ul{list-style:none;margin-top:18px}
.fcol li{font-size:9px;line-height:22px;color:#d8d8d8}
.vline{position:absolute;top:3362px;width:1px;height:224px;background:#444}
.contact-row{display:flex;align-items:center;gap:10px;font-size:9px;color:#d8d8d8;margin-top:16px}
.contact-row svg{width:18px;height:18px;flex:none}
.social{display:flex;gap:6px;position:absolute;left:121px;top:3550px}
.social span{width:18px;height:18px;border-radius:50%;border:1px solid #ddd}
.copyright{left:0;top:3598px;width:1200px;text-align:center;font-size:8.5px;color:#cfcfcf}
.fline{left:0;top:3588px;width:1200px;height:1px;background:#333}
</style>
</head>
<body>

<div class="abs topbar">Get a Smart Terminal POS device, fees starting at 2.3% for in-person transactions</div>

<header class="abs hero">
  <div class="abs" role="img" aria-label="Photo of a counsellor with notebook talking with a young man in a bright therapy room" style="inset:0"></div>
  <div class="abs hero-shade"></div>
</header>
<div class="abs brand" style="left:108px;top:42px;width:120px">
  <span class="mark"></span>
  <span class="name">Amber Crest</span>
  <span class="sub">Health &amp; Wellness Group</span>
</div>
<nav class="abs nav">
  <span class="active">Home</span><span>About</span><span>Services</span><span>Our Team</span><span>FAQ</span>
</nav>
<div class="btn btn-blue" style="left:950px;top:50px;width:128px;height:33px;font-size:10.5px">Contact Us
  <svg viewBox="0 0 12 12"><path d="M3 2l5 4-5 4" fill="none" stroke="#fff" stroke-width="2"/></svg></div>
<div class="abs eyebrow hero-eyebrow">Welcome to Amber Crest Health &amp; Wellness Group <span class="rule"></span></div>
<section class="abs hero" style="background:none;pointer-events:none">
  <h1 style="top:210px">HELPING THOSE<br>WHO HELP OTHERS</h1>
  <p style="top:327px">A dedicated space for mental health professionals, first responders, caregivers, and community members seeking effective healing and whole-person wellbeing.</p>
</section>
<div class="btn btn-blue" style="left:120px;top:411px;width:206px;height:39px">Book an Appointment
  <svg viewBox="0 0 12 12"><path d="M3 2l5 4-5 4" fill="none" stroke="#fff" stroke-width="2"/></svg></div>

<section class="about">
  <div class="abs about-photo"><div role="img" aria-label="Photo of a support group listening to a woman speaking"></div></div>
  <div class="abs eyebrow about-eyebrow">About Us <span class="rule"></span></div>
  <h2>ABOUT <span class="accent">AMBER CREST</span> HEALTH<br>&amp; WELLNESS GROUP</h2>
  <div class="tag">A clinic built on compassion, integrity &amp; clinical excellence</div>
  <p>We exist to provide <b>safe, professional, trauma-informed care</b> for individuals who dedicate their lives to serving others. Our team brings together registered <b>clinicians, wellness specialists, and rehabilitation professionals to deliver integrated</b> and personalized treatment.</p>
  <div class="ghost">AMBER CREST</div>
</section>
<div class="btn btn-blue" style="left:609px;top:931px;width:195px;height:39px">Learn More About Us
  <svg viewBox="0 0 12 12"><path d="M3 2l5 4-5 4" fill="none" stroke="#fff" stroke-width="2"/></svg></div>
<div class="btn btn-grey" style="left:811px;top:931px;width:151px;height:39px">Meet Our Team
  <svg viewBox="0 0 12 12"><path d="M3 2l5 4-5 4" fill="none" stroke="#fff" stroke-width="2"/></svg></div>

<section class="abs mission"></section>
<div class="abs emblem"><div>AMBER<br>CREST</div></div>
<div class="mv" style="left:122px;top:1174px">
  <svg viewBox="0 0 48 48" fill="none" stroke="#fff" stroke-width="3"><circle cx="22" cy="26" r="18"/><circle cx="22" cy="26" r="11"/><circle cx="22" cy="26" r="4"/><path d="M22 26L40 8M34 6l6 2 2 6"/></svg>
  <h3>OUR MISSION</h3>
  <p>To provide a professional, trauma-informed healing space where individuals who serve the community can receive exceptional care, restore balance, and reconnect with their wellbeing.</p>
</div>
<div class="mv" style="left:796px;top:1174px">
  <svg viewBox="0 0 48 48" fill="none" stroke="#fff" stroke-width="3"><path d="M4 28c8-10 32-10 40 0-8 10-32 10-40 0z"/><circle cx="24" cy="28" r="6"/><path d="M24 6v6M12 9l3 5M36 9l-3 5"/></svg>
  <h3>OUR VISION</h3>
  <p>To become a leading centre for integrated mental health and wellness—supporting resilience, reducing burnout, &amp; empowering healthy communities through compassionate, evidence based care.</p>
</div>

<section class="abs services-bg"></section>
<svg class="abs" style="left:0;top:2100px" width="1200" height="145" viewBox="0 0 1200 145"><path d="M0 50C300 160 700 150 1200 60V145H0Z" fill="#fff"/><path d="M0 50C300 160 700 150 1200 60" fill="none" stroke="#d9e2ee" stroke-width="3"/></svg>
<div class="abs eyebrow center-eyebrow" style="top:1486px"><span class="rule"></span>What We Do<span class="rule"></span></div>
<h2 class="section-title" style="top:1510px">OUR <span class="accent">SERVICES</span></h2>

<div class="card" style="left:121px;top:1570px"><div class="ph" role="img" aria-label="Photo of a soldier sitting in a therapy session"></div><div class="icon"><span><svg viewBox="0 0 16 16"><circle cx="8" cy="7" r="5" fill="#fff"/></svg></span></div><h4>Mental<br>Health Therapy</h4></div>
<div class="card" style="left:365px;top:1570px"><div class="ph" role="img" aria-label="Photo of paramedics in an ambulance" style="background:linear-gradient(135deg,#9aa4ac,#4a5a6a)"></div><div class="icon"><span><svg viewBox="0 0 16 16"><rect x="4" y="3" width="8" height="10" rx="2" fill="#fff"/></svg></span></div><h4>Trauma &amp; First<br>Responder Support</h4></div>
<div class="card" style="left:608px;top:1570px"><div class="ph" role="img" aria-label="Photo of hands spreading salt on a client's back" style="background:linear-gradient(135deg,#e8d8cc,#b89a88)"></div><div class="icon"><span><svg viewBox="0 0 16 16"><path d="M3 11h10l-2-5H5z" fill="#fff"/></svg></span></div><h4 class="one">Salt Therapy</h4></div>
<div class="card" style="left:850px;top:1570px"><div class="ph" role="img" aria-label="Photo of sound equipment and a mixing desk" style="background:linear-gradient(135deg,#d6d6d6,#5a5a5a)"></div><div class="icon"><span><svg viewBox="0 0 16 16" stroke="#fff" stroke-width="1.6"><path d="M3 6v4M6 4v8M9 3v10M12 6v4"/></svg></span></div><h4>Sound &amp;<br>Vibration Therapy</h4></div>

<div class="card" style="left:121px;top:1828px"><div class="ph" role="img" aria-label="Photo of a person wearing a light therapy headset" style="background:linear-gradient(135deg,#c07a6a,#3a2a2a)"></div><div class="icon"><span><svg viewBox="0 0 16 16"><circle cx="8" cy="6" r="3" fill="#fff"/><rect x="4" y="10" width="8" height="3" fill="#fff"/></svg></span></div><h4>Red<br>Light Therapy</h4></div>
<div class="card" style="left:365px;top:1828px"><div class="ph" role="img" aria-label="Photo of a client lying on a treatment mat" style="background:linear-gradient(135deg,#a89684,#4a3e34)"></div><div class="icon"><span><svg viewBox="0 0 16 16" fill="none" stroke="#fff" stroke-width="1.5"><path d="M8 13S2 9 2 5.5A3 3 0 0 1 8 4a3 3 0 0 1 6 1.5C14 9 8 13 8 13z"/></svg></span></div><h4 class="one">PEMF Therapy</h4></div>
<div class="card feature" style="left:608px;top:1828px"><div class="ph" role="img" aria-label="Photo of a patient wearing an EEG cap beside a clinician" style="background:linear-gradient(135deg,#7aa0c0,#2a4a6a)"></div><div class="icon"><span><svg viewBox="0 0 16 16"><circle cx="8" cy="8" r="5" fill="none" stroke="#fff" stroke-width="2" stroke-dasharray="3 2"/></svg></span></div><h4 class="one">Neurofeedback</h4></div>
<div class="card" style="left:850px;top:1828px"><div class="ph" role="img" aria-label="Photo of a surgical team in an operating room" style="background:linear-gradient(135deg,#b8ccd8,#5a7488)"></div><div class="icon"><span><svg viewBox="0 0 16 16"><circle cx="8" cy="4" r="2" fill="#fff"/><path d="M3 7h10l-3 2v5H6V9z" fill="#fff"/></svg></span></div><h4 class="one">OT &amp; Rehabilitation</h4></div>

<div class="btn btn-blue" style="left:510px;top:2084px;width:180px;height:38px">View All Services
  <svg viewBox="0 0 12 12"><path d="M3 2l5 4-5 4" fill="none" stroke="#fff" stroke-width="2"/></svg></div>

<div class="abs eyebrow center-eyebrow" style="top:2302px"><span class="rule"></span>Who We Serve<span class="rule"></span></div>
<h2 class="section-title" style="top:2324px">SUPPORT FOR THOSE IN <span class="accent">HIGH</span><br><span class="accent">IMPACT</span>, HIGH STRESS ROLES</h2>

<div class="serve" style="left:121px;top:2425px"><h5><svg viewBox="0 0 14 14"><circle cx="7" cy="7" r="7" fill="#245e9f"/><path d="M4 7l2 2 4-4" stroke="#fff" stroke-width="1.6" fill="none"/></svg>Mental Health Professionals</h5><p>navigating compassion fatigue and client load demands</p></div>
<div class="serve" style="left:473px;top:2425px"><h5><svg viewBox="0 0 14 14"><circle cx="7" cy="7" r="7" fill="#245e9f"/><path d="M4 7l2 2 4-4" stroke="#fff" stroke-width="1.6" fill="none"/></svg>First responders &amp; frontline Workers</h5><p>managing trauma exposure and high intensity environments</p></div>
<div class="serve" style="left:850px;top:2425px"><h5><svg viewBox="0 0 14 14"><circle cx="7" cy="7" r="7" fill="#245e9f"/><path d="M4 7l2 2 4-4" stroke="#fff" stroke-width="1.6" fill="none"/></svg>Healthcare Providers</h5><p>balancing patient care with personal wellbeing</p></div>
<div class="serve" style="left:121px;top:2519px"><h5><svg viewBox="0 0 14 14"><circle cx="7" cy="7" r="7" fill="#245e9f"/><path d="M4 7l2 2 4-4" stroke="#fff" stroke-width="1.6" fill="none"/></svg>Educators &amp; Social Service Workers</h5><p>experiencing burnout, stress, and emotional strain</p></div>
<div class="serve" style="left:473px;top:2519px"><h5><svg viewBox="0 0 14 14"><circle cx="7" cy="7" r="7" fill="#245e9f"/><path d="M4 7l2 2 4-4" stroke="#fff" stroke-width="1.6" fill="none"/></svg>Individuals Healing from Trauma</h5><p>seeking trauma-informed, evidence based support</p></div>
<div class="serve" style="left:850px;top:2519px"><h5><svg viewBox="0 0 14 14"><circle cx="7" cy="7" r="7" fill="#245e9f"/><path d="M4 7l2 2 4-4" stroke="#fff" stroke-width="1.6" fill="none"/></svg>Families Seeking Guidance</h5><p>for emotional, behavioural, or stress -related challenges</p></div>

<div class="btn btn-blue" style="left:497px;top:2609px;width:206px;height:38px">Explore How We Help
  <svg viewBox="0 0 12 12"><path d="M3 2l5 4-5 4" fill="none" stroke="#fff" stroke-width="2"/></svg></div>

<h2 class="section-title" style="top:2702px">OUR COMMUNITY <span class="accent">PARTNERS</span></h2>
<svg class="arrow" style="left:116px;top:2806px" viewBox="0 0 14 14"><path d="M9 2L4 7l5 5" fill="none" stroke="#245e9f" stroke-width="1.6"/></svg>
<div class="abs partners">
  <div class="partner"><i></i>Northgate Care</div>
  <div class="partner"><i></i>Harbourline Guild</div>
  <div class="partner"><i></i>Keystone Chiro</div>
  <div class="partner"><i></i>Riverbend Health</div>
  <div class="partner"><i></i>Brightpath</div>
</div>
<svg class="arrow" style="left:1070px;top:2806px" viewBox="0 0 14 14"><path d="M5 2l5 5-5 5" fill="none" stroke="#245e9f" stroke-width="1.6"/></svg>

<section class="abs cta"></section>
<div class="abs cta-person" role="img" aria-label="Photo of a smiling doctor in a white coat with a stethoscope pointing left"></div>
<section class="cta" style="position:static">
  <h2>TAKE THE FIRST STEP<br>TOWARD HEALING</h2>
  <p>Begin your journey with a team that understands the unique challenges faced by caregivers, first responders, and helping professionals.</p>
</section>
<div class="btn btn-white" style="left:142px;top:3177px;width:206px;height:38px">Book an Appointment
  <svg viewBox="0 0 12 12"><path d="M3 2l5 4-5 4" fill="none" stroke="#245e9f" stroke-width="2"/></svg></div>

<footer class="abs footer"></footer>
<div class="abs brand" style="left:116px;top:3372px;width:120px">
  <span class="mark"></span>
  <span class="name">Amber Crest</span>
  <span class="sub">Health &amp; Wellness Group</span>
</div>
<p class="abs" style="left:121px;top:3474px;width:170px;font-size:9px;line-height:14px;color:#d8d8d8">We exist to provide safe, professional, trauma-informed care for individuals who dedicate their lives to serving others.</p>
<div class="social"><span></span><span></span><span></span></div>
<div class="vline" style="left:297px"></div>
<div class="vline" style="left:534px"></div>
<div class="vline" style="left:850px"></div>
<div class="fcol" style="left:314px;top:3368px">
  <h6>Contact Us</h6>
  <div class="contact-row" style="margin-top:20px"><svg viewBox="0 0 18 18"><circle cx="9" cy="9" r="8.5" fill="none" stroke="#ddd"/><path d="M9 4a3 3 0 0 1 3 3c0 2-3 6-3 6S6 9 6 7a3 3 0 0 1 3-3z" fill="#ddd"/></svg>Maple Harbour, Ontario</div>
  <div class="contact-row"><svg viewBox="0 0 18 18"><circle cx="9" cy="9" r="8.5" fill="none" stroke="#ddd"/><rect x="5" y="6" width="8" height="6" fill="#ddd"/></svg><span style="color:#6aa4e6">info@ambercresthealthandwellnessgroup.ca</span></div>
</div>
<div class="fcol" style="left:559px;top:3368px"><h6>Main Links</h6><ul><li>About</li><li>Services</li><li>Our Team</li><li>FAQ</li><li>Contact Us</li></ul></div>
<div class="fcol" style="left:687px;top:3368px"><h6>Our Services</h6><ul><li>Mental Health Therapy</li><li>Trauma &amp; First Responder support</li><li>Salt Therapy</li><li>Sound &amp; Vibration Therapy</li><li>Red-Light Therapy</li><li>PEMF Therapy</li><li>Neurofeedback</li><li>OT &amp; Rehabilitation</li></ul></div>
<div class="fcol" style="left:868px;top:3368px"><h6>Subscribe Newsletter</h6></div>
<div class="abs" style="left:871px;top:3409px;width:171px;height:31px;border:1px solid #bbb;font-size:9px;color:#ccc;padding:9px 12px">Enter Your Email</div>
<div class="btn btn-blue" style="left:871px;top:3460px;width:132px;height:38px">Subscribe
  <svg viewBox="0 0 12 12"><path d="M3 2l5 4-5 4" fill="none" stroke="#fff" stroke-width="2"/></svg></div>
<div class="abs fline"></div>
<div class="abs copyright">©2025 Amber Crest Health &amp; Wellness Group All Rights Reserved.</div>

</body>
</html>
```